Business Card design which attached logo. Company is called Tallowind Shield and main colours are Orange & Black.

Company specialises in Paint Protection and Detailing for supercars.

Details needed on business card:

Sales

Address: Unit 14, 172 Garrick Road, Wexley Vale, NSW 2381

Phone: 02 9461 2738

website: www.tallowindshield.com.au

Email: sales@tallowindshield.com.au

```html
<!DOCTYPE html>
<html lang="en">
<head>
<meta charset="utf-8">
<title>Tallowind Shield – Business Card</title>
<link href="https://fonts.googleapis.com/css2?family=Montserrat:wght@300;400;500&display=swap" rel="stylesheet">
<style>
  :root {
    --orange: #f0571e;
    --black: #0a0a0b;
    --ink: #111113;
    --white: #ffffff;
    --grey: #6b6b6b;
    --stage: #2a2c30;
  }
  * { margin: 0; padding: 0; box-sizing: border-box; }
  html, body { width: 1200px; height: 900px; overflow: hidden; }
  body {
    background: var(--stage);
    font-family: "Montserrat", Arial, sans-serif;
    position: relative;
  }
  .card {
    position: absolute;
    left: 250px;
    width: 700px;
    height: 400px;
    background: var(--black);
    overflow: hidden;
    box-shadow: 0 10px 30px rgba(0,0,0,.45);
  }
  .card--front { top: 36px; }
  .card--back { top: 464px; }

  .card__wave { position: absolute; inset: 0; }

  .card__artwork {
    position: absolute;
    left: 330px; top: 34px;
    width: 270px; height: 130px;
    background: radial-gradient(ellipse at center, #2a1a12 0%, var(--ink) 70%);
  }
  .brand-name {
    position: absolute;
    color: var(--orange);
    font-weight: 300;
    text-transform: uppercase;
    letter-spacing: 2px;
    white-space: nowrap;
  }
  .card--front .brand-name { left: 400px; top: 172px; font-size: 22px; }

  .person { position: absolute; left: 34px; top: 200px; }
  .person__name {
    color: var(--orange);
    font-weight: 500;
    font-size: 26px;
    letter-spacing: 1px;
    text-transform: uppercase;
  }
  .person__address {
    margin-top: 6px;
    color: var(--grey);
    font-size: 15px;
    line-height: 21px;
    font-weight: 400;
  }
  .contacts {
    position: absolute;
    left: 34px; top: 294px;
    padding-left: 18px;
    border-left: 1px solid var(--grey);
    list-style: none;
  }
  .contacts__item {
    display: flex; align-items: center; gap: 10px;
    color: #444;
    font-size: 15px;
    line-height: 26px;
  }
  .contacts__icon { width: 14px; height: 14px; fill: var(--orange); flex: none; }

  .card__pattern {
    position: absolute; inset: 0;
    background: linear-gradient(135deg, #0d0d0f 0%, #141417 60%, #0d0d0f 100%);
  }
  .card--back .brand-name {
    left: 0; right: 0; top: 178px;
    text-align: center;
    font-size: 34px;
    letter-spacing: 3px;
  }
</style>
</head>
<body>

  <section class="card card--front" aria-label="Business card front">
    <svg class="card__wave" viewBox="0 0 700 400" aria-hidden="true">
      <path d="M0,112 C230,112 450,222 570,400" fill="none" stroke="var(--orange)" stroke-width="3"/>
      <path d="M0,126 C225,126 440,232 556,400" fill="none" stroke="var(--orange)" stroke-width="2"/>
      <path d="M0,142 C220,142 430,246 540,400" fill="none" stroke="#000" stroke-width="14"/>
      <path d="M0,150 C220,150 425,252 532,400 L0,400 Z" fill="var(--white)"/>
    </svg>

    <div class="card__artwork" role="img" aria-label="Orange line drawing of a supercar"></div>
    <p class="brand-name">Tallowind Shield</p>

    <div class="person">
      <h1 class="person__name">Liam Harlow</h1>
      <p class="person__address">Unit 14, 172 Garrick Road<br>Wexley Vale, NSW 2381</p>
    </div>

    <ul class="contacts">
      <li class="contacts__item">
        <svg class="contacts__icon" viewBox="0 0 24 24"><path d="M6.6 10.8a15 15 0 0 0 6.6 6.6l2.2-2.2c.3-.3.7-.4 1-.2 1.1.4 2.3.6 3.6.6.6 0 1 .4 1 1V20c0 .6-.4 1-1 1A17 17 0 0 1 3 4c0-.6.4-1 1-1h3.5c.6 0 1 .4 1 1 0 1.3.2 2.5.6 3.6.1.3 0 .7-.2 1z"/></svg>
        02 9461 2738
      </li>
      <li class="contacts__item">
        <svg class="contacts__icon" viewBox="0 0 24 24"><path d="M2 5h20v14H2z M2 5l10 8 10-8" fill="none" stroke="var(--orange)" stroke-width="2"/></svg>
        sales@tallowindshield.com.au
      </li>
      <li class="contacts__item">
        <svg class="contacts__icon" viewBox="0 0 24 24"><circle cx="12" cy="12" r="10" fill="none" stroke="var(--orange)" stroke-width="2"/><path d="M2 12h20M12 2c3 3 3 17 0 20M12 2c-3 3-3 17 0 20" fill="none" stroke="var(--orange)" stroke-width="1.6"/></svg>
        www.tallowindshield.com.au
      </li>
    </ul>
  </section>

  <section class="card card--back" aria-label="Business card back">
    <div class="card__pattern" role="img" aria-label="Faint dark repeating brand pattern"></div>
    <p class="brand-name">Tallowind Shield</p>
  </section>

</body>
</html>
```